Brightpath Home Partners, LLC

We are private duty home care agency. We provide in-home care for people of all ages. Our kind natured and patient caregivers provide assistance to those who have difficulty with caring for themselves. We already have a logo designed by ArtMarketly

```html
<!DOCTYPE html>
<html lang="en">
<head>
<meta charset="utf-8">
<title>Brightpath Home Partners, LLC</title>
<link rel="stylesheet" href="https://fonts.googleapis.com/css2?family=Lato:wght@400;700&family=Raleway:wght@500;600;700&display=swap">
<style>
:root{
  --orange:#f96508;
  --green:#2a8a06;
  --lime:#8fe31a;
  --ink:#222222;
  --text:#4d4d4d;
  --grey-panel:#ebebeb;
  --footer:#ececec;
  --white:#ffffff;
}
*{margin:0;padding:0;box-sizing:border-box}
html,body{width:1200px;height:3558px;overflow:hidden}
body{position:relative;background:var(--white);font-family:'Lato',sans-serif;color:var(--text)}
.abs{position:absolute}
.heading{font-family:'Raleway',sans-serif;font-weight:700}
.btn{position:absolute;display:flex;align-items:center;justify-content:center;font-family:'Raleway',sans-serif;font-weight:700;color:var(--white);text-transform:uppercase;letter-spacing:.3px}
.section-mark{width:34px;height:34px;border-radius:50%}

/* header */
.logo{left:140px;top:26px;color:var(--green);font-family:'Raleway',sans-serif;font-weight:700;font-size:21px;line-height:25px}
.main-nav{left:412px;top:48px;font-size:17px;color:var(--ink)}
.main-nav span{position:absolute;white-space:nowrap}
.phone{left:932px;top:44px;font-size:18px;font-weight:700;color:var(--ink);display:flex;align-items:center;gap:6px;white-space:nowrap}

/* hero */
.hero{left:0;top:0;width:1200px;height:705px;background:linear-gradient(90deg,#f4f4f2 0%,#f1efec 35%,#e3d8cf 55%,#c9b6a4 75%,#b6a28f 100%)}
.hero-title{left:145px;width:400px;top:293px;text-align:center;color:var(--green);font-size:35px;line-height:40px}
.hero-sub{left:145px;width:400px;top:331px;text-align:center;color:var(--orange);font-size:26px}
.hero-copy{left:145px;width:400px;top:377px;text-align:center;font-size:16px;line-height:23px;color:var(--ink)}
.hero .btn{left:239px;top:447px;width:210px;height:47px;background:var(--orange);font-size:17px}
.slide-arrow{width:60px;height:60px;border-radius:50%;background:rgba(120,120,120,.55);display:flex;align-items:center;justify-content:center}

/* about */
.about-title{left:615px;top:797px;font-size:36px;color:var(--green);white-space:nowrap}
.about-title b{color:var(--orange)}
.lead{font-size:18px;line-height:26px;color:var(--text)}
.body{font-size:16px;line-height:27px;color:var(--text)}

/* services */
.services-title{left:0;width:1200px;text-align:center;top:1293px;color:var(--white);font-size:30px}
.service{color:var(--white)}
.service h3{font-family:'Raleway',sans-serif;font-weight:700;font-size:19px;line-height:23px;margin-bottom:12px}
.service p{font-size:14px;line-height:23px;opacity:.9}
.outline-btn{left:486px;top:1717px;width:222px;height:50px;border:2px solid var(--white);font-size:15px;font-weight:600}

/* why */
.why-photo{left:0;top:1760px;width:604px;height:574px;background:linear-gradient(135deg,#e9e4de 0%,#d8cfc6 45%,#b9aa9b 100%)}
.why-panel{left:604px;top:1810px;width:596px;height:524px;background:var(--grey-panel)}
.why-title{left:667px;top:1928px;font-size:31px;color:#454545;font-weight:600}

/* testimonials */
.testi-title{left:0;width:1200px;text-align:center;top:2424px;font-size:26px;color:var(--white);font-weight:500}
.quote{left:452px;top:2466px;width:505px;font-size:18px;line-height:32px;color:var(--white)}
.quote-mark{font-family:Georgia,serif;font-size:56px;color:var(--white);line-height:1}
.testi-name{left:452px;top:2610px;font-size:17px;font-weight:700;color:var(--white)}

/* blogs */
.blogs-title{left:0;width:1200px;text-align:center;top:2812px;color:var(--orange);font-size:34px}
.blog-date{font-size:13px;font-weight:700;color:var(--orange);white-space:nowrap}
.blog-head{font-size:18px;line-height:24px;color:var(--ink);text-transform:uppercase}
.blog-more{font-size:15px;font-weight:700;color:var(--green)}
.thumb{background:linear-gradient(135deg,#dcd6cf 0%,#b7c3cf 55%,#8fa1b4 100%)}
.divider{left:635px;width:417px;height:1px;background:#cfcfcf}

/* footer */
.footer{left:0;top:3405px;width:1200px;height:153px;background:var(--footer);border-top:3px solid #dddddd}
.foot-nav{font-size:17px;color:var(--ink);white-space:nowrap;top:3455px}
.social{width:32px;height:32px;border-radius:50%;background:#2a5ea8;top:3448px}
.copyright{left:174px;top:3494px;font-size:12px;color:var(--ink)}
</style>
</head>
<body>

<!-- hero -->
<section class="abs hero">
  <div class="abs" style="left:560px;top:90px;width:640px;height:615px;background:linear-gradient(120deg,#efe7df 0%,#d5c3b3 45%,#9d8b7a 100%);opacity:.75" role="img" aria-label="Photo of a caregiver checking an elderly woman's heartbeat on a sofa"></div>
  <span class="abs section-mark" style="left:328px;top:228px;background:var(--orange)"></span>
  <h1 class="abs heading hero-title">LIVE INDEPENDENTLY</h1>
  <p class="abs heading hero-sub">IN YOUR OWN HOME</p>
  <p class="abs hero-copy">Lorem ipsum dolor sit amet consectetuer<br>adipiscing elit Nam cursus Morbi</p>
  <a class="btn">Get a free call</a>
  <div class="abs slide-arrow" style="left:56px;top:329px"><svg width="18" height="26" viewBox="0 0 18 26"><path d="M14 3 L4 13 L14 23" fill="none" stroke="#fff" stroke-width="3"/></svg></div>
  <div class="abs slide-arrow" style="left:1075px;top:329px"><svg width="18" height="26" viewBox="0 0 18 26"><path d="M4 3 L14 13 L4 23" fill="none" stroke="#fff" stroke-width="3"/></svg></div>
</section>

<!-- header -->
<header>
  <div class="abs logo">Brightpath<br>Home Partners, LLC</div>
  <nav class="abs main-nav">
    <span style="left:0">About Us</span>
    <span style="left:100px">Our Services</span>
    <span style="left:227px">Blogs</span>
    <span style="left:299px">Testimonial</span>
    <span style="left:424px">Contact</span>
  </nav>
  <div class="abs phone">
    <svg width="18" height="18" viewBox="0 0 24 24"><path fill="#2a8a06" d="M6.6 10.8a15.1 15.1 0 0 0 6.6 6.6l2.2-2.2c.3-.3.7-.4 1-.2 1.1.4 2.3.6 3.6.6.6 0 1 .4 1 1V20c0 .6-.4 1-1 1C10.6 21 3 13.4 3 4c0-.6.4-1 1-1h3.5c.6 0 1 .4 1 1 0 1.3.2 2.5.6 3.6.1.3 0 .7-.2 1z"/></svg>
    685 555 0142
  </div>
</header>

<!-- about -->
<section>
  <svg class="abs" style="left:160px;top:748px" width="416" height="416" viewBox="0 0 416 416">
    <circle cx="206" cy="206" r="204" fill="var(--lime)"/>
    <circle cx="214" cy="208" r="198" fill="var(--orange)"/>
    <circle cx="216" cy="210" r="185" fill="#e3d5c8"/>
  </svg>
  <div class="abs" style="left:191px;top:773px;width:370px;height:370px;border-radius:50%;background:linear-gradient(135deg,#e8dccf 0%,#cbb6a2 50%,#9c8570 100%)" role="img" aria-label="Photo of a smiling caregiver with an elderly woman"></div>
  <h2 class="abs heading about-title">ABOUT <b>BRIGHTPATH</b></h2>
  <p class="abs lead" style="left:615px;top:862px;width:415px">Pellentesque faucibus Ut accumsan ultricies elit Maecenas at justo id velit placerat molestie</p>
  <p class="abs body" style="left:615px;top:927px;width:430px">Enim iaculis aliquam Mauris nunc quam venenatis nec euismod sit amet egestas placerat est Pellentesque habitant morbi tristique senectus et netus et malesuada fames ac turpis egestas Cras id elit Integer quis urna</p>
  <a class="btn" style="left:615px;top:1069px;width:180px;height:48px;background:var(--orange);font-size:18px">Learn more</a>
</section>

<!-- why (placed before the services band so the band's curved edge sits on top) -->
<section>
  <div class="abs why-panel"></div>
  <div class="abs why-photo" role="img" aria-label="Photo of a caregiver helping an elderly woman walk with crutches"></div>
  <h2 class="abs heading why-title">WHY WE ARE</h2>
  <p class="abs lead" style="left:668px;top:1987px;width:420px;line-height:24px">Pellentesque faucibus Ut accumsan ultricies elit Maecenas at justo id velit placerat molestie</p>
  <p class="abs body" style="left:668px;top:2045px;width:460px;line-height:23.5px">Enim iaculis aliquam Mauris nunc quam venenatis nec euismod sit amet egestas placerat est Pellentesque habitant morbi tristique senectus et netus et malesuada fames ac turpis egestas Cras id elit Integer quis urna</p>
  <a class="btn" style="left:668px;top:2168px;width:171px;height:46px;background:var(--green);font-size:18px">Learn more</a>
</section>

<!-- services band -->
<section>
  <svg class="abs" style="left:0;top:1200px" width="1200" height="640" viewBox="0 0 1200 640">
    <path d="M0 26 C300 10 620 0 900 50 C1030 74 1130 110 1200 140 L1200 160 C1100 120 1000 96 860 80 Z" fill="var(--lime)"/>
    <path d="M0 26 C300 10 620 2 880 52 C1020 80 1120 118 1200 152 L1200 612 C900 620 500 610 260 590 C140 578 50 560 0 548 Z" fill="var(--orange)"/>
    <path d="M0 520 C120 560 300 594 560 612 C800 626 1000 622 1200 612 L1200 618 C900 630 500 626 260 610 C140 600 50 590 0 584 Z" fill="var(--lime)"/>
  </svg>
  <span class="abs section-mark" style="left:581px;top:1250px;background:var(--white)"></span>
  <h2 class="abs heading services-title">OUR SERVICES</h2>

  <svg class="abs" style="left:95px;top:1503px" width="30" height="34" viewBox="0 0 30 34"><path d="M22 3 L8 17 L22 31" fill="none" stroke="#fff" stroke-width="3.5"/></svg>
  <svg class="abs" style="left:1058px;top:1503px" width="30" height="34" viewBox="0 0 30 34"><path d="M8 3 L22 17 L8 31" fill="none" stroke="#fff" stroke-width="3.5"/></svg>

  <svg class="abs" style="left:175px;top:1360px" width="116" height="116" viewBox="0 0 116 116"><path d="M58 4 A54 54 0 1 1 4 58" fill="none" stroke="#fff" stroke-width="4"/><circle cx="62" cy="56" r="30" fill="rgba(255,255,255,.22)" role="img" aria-label="Icon of helping hands"/></svg>
  <svg class="abs" style="left:626px;top:1360px" width="116" height="116" viewBox="0 0 116 116"><path d="M58 4 A54 54 0 1 1 4 58" fill="none" stroke="#fff" stroke-width="4"/><circle cx="62" cy="56" r="30" fill="rgba(255,255,255,.22)" role="img" aria-label="Icon of a meal plate"/></svg>
  <svg class="abs" style="left:175px;top:1540px" width="116" height="116" viewBox="0 0 116 116"><path d="M58 4 A54 54 0 1 1 4 58" fill="none" stroke="#fff" stroke-width="4"/><circle cx="62" cy="56" r="30" fill="rgba(255,255,255,.22)" role="img" aria-label="Icon of cleaning supplies"/></svg>
  <svg class="abs" style="left:626px;top:1544px" width="116" height="116" viewBox="0 0 116 116"><path d="M58 4 A54 54 0 1 1 4 58" fill="none" stroke="#fff" stroke-width="4"/><circle cx="62" cy="56" r="30" fill="rgba(255,255,255,.22)" role="img" aria-label="Icon of medication capsules"/></svg>

  <div class="abs service" style="left:302px;top:1375px;width:300px"><h3>Help with Personal<br>Hygiene and Care</h3><p>Pellentesque faucibus Ut accumsan ultricies elit Maecenas at justo id velit placerat</p></div>
  <div class="abs service" style="left:753px;top:1375px;width:300px"><h3>Assisting with Meals<br>and Nutrition</h3><p>Pellentesque faucibus Ut accumsan ultricies elit Maecenas at justo id velit placerat</p></div>
  <div class="abs service" style="left:302px;top:1555px;width:300px"><h3>Home Maintenance and<br>Housekeeping</h3><p>Pellentesque faucibus Ut accumsan ultricies elit Maecenas at justo id velit placerat</p></div>
  <div class="abs service" style="left:753px;top:1559px;width:300px"><h3>Prescription Medication<br>Management</h3><p>Pellentesque faucibus Ut accumsan ultricies elit Maecenas at justo id velit placerat</p></div>

  <a class="btn outline-btn">View more serivces</a>
</section>

<!-- testimonials -->
<section>
  <svg class="abs" style="left:0;top:2320px" width="1200" height="460" viewBox="0 0 1200 460">
    <path d="M0 14 C300 4 700 8 1000 60 C1100 78 1160 94 1200 104 L1200 128 C1100 100 1000 84 880 70 Z" fill="var(--orange)"/>
    <path d="M0 14 C300 4 700 10 960 60 C1080 84 1150 108 1200 122 L1200 440 C900 446 500 444 260 430 C140 420 50 404 0 392 Z" fill="var(--green)"/>
    <path d="M0 356 C150 400 350 426 600 436 C850 446 1050 444 1200 440 L1200 446 C900 452 500 452 260 442 C140 436 50 420 0 410 Z" fill="var(--orange)"/>
  </svg>
  <span class="abs section-mark" style="left:590px;top:2364px;background:var(--white)"></span>
  <h2 class="abs heading testi-title">TESTIMONIALS</h2>
  <svg class="abs" style="left:230px;top:2467px" width="184" height="180" viewBox="0 0 184 180">
    <circle cx="90" cy="88" r="86" fill="var(--lime)"/>
    <circle cx="96" cy="90" r="82" fill="var(--orange)"/>
    <circle cx="94" cy="88" r="74" fill="#ffffff"/>
  </svg>
  <div class="abs" style="left:250px;top:2483px;width:148px;height:148px;border-radius:50%;background:linear-gradient(135deg,#d9dde3 0%,#b8bec6 55%,#8c949e 100%)" role="img" aria-label="Portrait photo of a smiling senior client"></div>
  <div class="abs quote-mark" style="left:405px;top:2458px">&ldquo;</div>
  <p class="abs quote">Sed ut perspiciatis unde omnis iste natus error sit voluptatem accusantium doloremque laudantium, totam rem aperiam, eaque ipsa quae ab illo inventore veritatis et quasi architecto beatae vitae dicta sunt explicabo. <span class="quote-mark" style="font-size:56px;vertical-align:-26px">&rdquo;</span></p>
  <p class="abs testi-name">DANIEL MOORE</p>
  <svg class="abs" style="left:163px;top:2524px" width="26" height="34" viewBox="0 0 26 34"><path d="M20 3 L6 17 L20 31" fill="none" stroke="#fff" stroke-width="3.5"/></svg>
  <svg class="abs" style="left:1018px;top:2524px" width="26" height="34" viewBox="0 0 26 34"><path d="M6 3 L20 17 L6 31" fill="none" stroke="#fff" stroke-width="3.5"/></svg>
</section>

<!-- recent blogs -->
<section>
  <h2 class="abs heading blogs-title">RECENT BLOGS</h2>

  <div class="abs thumb" style="left:164px;top:2894px;width:430px;height:244px" role="img" aria-label="Photo of a caregiver and an elderly couple reviewing paperwork"></div>
  <p class="abs blog-date" style="left:174px;top:3166px">April 12, 2019 &nbsp;| &nbsp;No Comments</p>
  <h3 class="abs blog-head" style="left:174px;top:3190px;width:420px">Mauris vel lacus vitae felis vestibulum volutpat etiam est nunc</h3>
  <p class="abs" style="left:174px;top:3252px;width:410px;font-size:13px;line-height:22px;color:var(--text)">Nunc tempus felis vitae urna Vivamus porttitor neque at volutpat rutrum purus nisi eleifend libero a tempus libero lectus</p>
  <p class="abs blog-more" style="left:176px;top:3306px">Learn More</p>

  <div class="abs thumb" style="left:635px;top:2894px;width:127px;height:119px" role="img" aria-label="Photo of a caregiver with an elderly man"></div>
  <p class="abs blog-date" style="left:791px;top:2902px">April 08, 2019 &nbsp;| &nbsp;No Comments</p>
  <h3 class="abs blog-head" style="left:791px;top:2926px;width:265px">Mauris vel lacus vitae<br>felis vestibulum volutpat</h3>
  <p class="abs blog-more" style="left:791px;top:2984px">Learn More</p>
  <div class="abs divider" style="top:3031px"></div>

  <div class="abs thumb" style="left:635px;top:3055px;width:127px;height:118px" role="img" aria-label="Photo of a caregiver serving a meal at home"></div>
  <p class="abs blog-date" style="left:792px;top:3052px">April 06, 2019 &nbsp;| &nbsp;No Comments</p>
  <h3 class="abs blog-head" style="left:792px;top:3076px;width:265px">Fusce tellus sed metus<br>augue convallis et</h3>
  <p class="abs blog-more" style="left:792px;top:3134px">Learn More</p>
  <div class="abs divider" style="top:3194px"></div>

  <div class="abs thumb" style="left:637px;top:3215px;width:127px;height:119px" role="img" aria-label="Photo of a nurse attending a patient in bed"></div>
  <p class="abs blog-date" style="left:794px;top:3216px">April 02, 2019 &nbsp;| &nbsp;No Comments</p>
  <h3 class="abs blog-head" style="left:794px;top:3240px;width:265px">Phasellus felis dolor<br>scelerisque a tempus</h3>
  <p class="abs blog-more" style="left:794px;top:3298px">Learn More</p>
</section>

<!-- footer -->
<footer>
  <div class="abs footer"></div>
  <span class="abs foot-nav" style="left:174px">Home</span>
  <span class="abs foot-nav" style="left:250px">About Us</span>
  <span class="abs foot-nav" style="left:352px">Our Services</span>
  <span class="abs foot-nav" style="left:479px">Blogs</span>
  <span class="abs foot-nav" style="left:552px">Why Us</span>
  <span class="abs foot-nav" style="left:642px">Testimonial</span>
  <span class="abs foot-nav" style="left:762px">Contact</span>
  <span class="abs social" style="left:894px"></span>
  <span class="abs social" style="left:933px;background:#2f8bd6"></span>
  <span class="abs social" style="left:970px;background:#2a5ea8"></span>
  <span class="abs social" style="left:1009px;background:#1f63a8"></span>
  <p class="abs copyright">&copy; 2019 Company Name &nbsp;All right reserved</p>
</footer>

</body>
</html>
```